Tarvexa website

Web design for small consulting firm
It can be simple, easy to find approach

The primary use is business to business for

a. people wanting to find out a bit more of us after receiving a business card
b. Search words to draw people from search engines to us

See MS Word doc with more info

Target Market(s)

Senior staff of large companies, in their work capacity
MD / CEO / CFO , directors, etc.

Industry/Entity Type

Business

Colors
ffffff
f79020
faa54b
33a6d7

```html
<!DOCTYPE html>
<html lang="en">
<head>
<meta charset="utf-8">
<title>Tarvexa Insight</title>
<link href="https://fonts.googleapis.com/css2?family=Open+Sans:wght@400;600;700&display=swap" rel="stylesheet">
<style>
:root{
  --white:#ffffff;
  --page:#fbfdfd;
  --orange:#e8872a;
  --orange-light:#faa54b;
  --blue:#1a7ab8;
  --blue-dark:#0d4f86;
  --sky:#33a6d7;
  --text:#333333;
  --muted:#808080;
  --rule:#c9c9c9;
  --band:#5b5b5b;
  --foot:#e4e4e4;
}
*{margin:0;padding:0;box-sizing:border-box}
html,body{width:1024px;height:1200px;overflow:hidden;background:var(--page)}
body{font-family:'Open Sans',sans-serif;color:var(--text);position:relative}
.header{position:absolute;left:0;top:0;width:1024px;height:76px;background:var(--white)}
.brand{position:absolute;left:138px;top:22px;display:flex;align-items:center;gap:10px;font-size:26px;font-weight:700;color:var(--blue);line-height:1}
.brand-mark{width:14px;height:14px;background:var(--orange)}
.call{position:absolute;right:135px;top:30px;font-size:13px;color:var(--muted);display:flex;align-items:center;gap:6px}
.call strong{color:var(--blue-dark);font-weight:600}
.call-icon{width:18px;height:18px;background:var(--blue-dark);border-radius:2px;display:flex;align-items:center;justify-content:center}
.nav{position:absolute;top:76px;left:0;width:1024px;height:40px;background:var(--orange)}
.nav a{position:absolute;top:12px;color:var(--white);font-size:13.5px;font-weight:700;letter-spacing:2.2px;text-decoration:none}
.hero{position:absolute;top:116px;left:0;width:1024px;height:313px;background:linear-gradient(90deg,#e9d6c6 0%,#d9b39d 25%,#6d88a8 45%,#d58aa0 55%,#c7c3bd 100%)}
.hero-panel{position:absolute;top:116px;left:538px;width:383px;height:313px;background:linear-gradient(180deg,rgba(10,90,130,.92),rgba(8,70,120,.95))}
.hero-panel h1{position:absolute;left:36px;top:96px;font-size:29px;font-weight:700;color:var(--white);white-space:nowrap}
.hero-panel p{position:absolute;left:36px;top:150px;width:312px;font-size:14.4px;line-height:20px;color:var(--white)}
.heading{position:absolute;font-size:20.5px;font-weight:600;color:var(--blue);white-space:nowrap}
.rule{position:absolute;height:4px;border-top:1px dotted var(--rule);border-bottom:1px dotted var(--rule)}
.photo{position:absolute;border-radius:3px}
.body-text{position:absolute;font-size:9.6px;line-height:15px;color:var(--text)}
.more{position:absolute;font-size:10px;font-weight:600;color:var(--blue-dark);text-decoration:underline}
.news-title{position:absolute;left:651px;font-size:12px;font-weight:600;color:var(--text);white-space:nowrap}
.news-text{position:absolute;left:730px;width:160px;font-size:9.4px;line-height:14.4px;color:var(--muted)}
.news-date{position:absolute;left:730px;font-size:7.5px;font-weight:700;color:var(--muted)}
.clients{position:absolute;top:1029px;left:0;width:1024px;height:87px;background:var(--band)}
.client{position:absolute;top:32px;color:var(--white);font-size:15px;font-weight:700;display:flex;align-items:center;gap:6px}
.client i{display:inline-block;width:12px;height:12px;background:var(--white);border-radius:50%}
.footer{position:absolute;top:1116px;left:0;width:1024px;height:84px;background:var(--foot)}
.links{position:absolute;left:138px;top:28px;font-size:10.5px;font-weight:700;color:#3b4f66;letter-spacing:.8px}
.copy{position:absolute;left:137px;top:51px;font-size:10px;color:#3b4f66}
.social{position:absolute;top:27px;display:flex;align-items:center}
.social i{display:inline-block;width:20px;height:20px;border-radius:50%}
.contact{position:absolute;left:746px;font-size:10px;color:#3b4f66;display:flex;align-items:center;gap:10px}
</style>
</head>
<body>
<header class="header">
  <div class="brand"><span class="brand-mark"></span>Tarvexa Insight</div>
  <div class="call"><span class="call-icon"><svg width="10" height="10" viewBox="0 0 24 24"><path fill="#fff" d="M6.6 10.8a15 15 0 0 0 6.6 6.6l2.2-2.2c.3-.3.7-.4 1-.2 1.1.4 2.3.6 3.6.6.6 0 1 .4 1 1V20c0 .6-.4 1-1 1A17 17 0 0 1 3 4c0-.6.4-1 1-1h3.5c.6 0 1 .4 1 1 0 1.3.2 2.5.6 3.6.1.3 0 .7-.2 1z"/></svg></span>CALL US TODAY <strong>+1 555 014 2290</strong></div>
</header>
<nav class="nav">
  <a style="left:142px">HOME</a><a style="left:268px">SERVICES</a><a style="left:418px">BLOG</a><a style="left:541px">ABOUT</a><a style="left:674px">CLIENTS</a><a style="left:816px">CONTACT</a>
</nav>
<div class="hero" role="img" aria-label="Photo of smiling colleagues in an office"></div>
<div class="hero-panel">
  <h1>WE MAKE IT HAPPEN.</h1>
  <p>It is a long established fact that a reader will be distracted by the readable content of a page when looking at its layout.</p>
</div>

<h2 class="heading" style="left:138px;top:460px">Welcome To Tarvexa Insight</h2>
<div class="rule" style="left:137px;top:499px;width:479px"></div>
<div class="photo" role="img" aria-label="Photo of a smiling businesswoman with her team" style="left:138px;top:514px;width:238px;height:167px;background:linear-gradient(135deg,#c9d6e3,#a7bed6 50%,#e7ddd4)"></div>
<p class="body-text" style="left:394px;top:516px;width:225px">Lorem ipsum dolor sit amet, consectetur adipisic-ing elit, sed do eiusmod tempor incididunt ut labore et dolore magna aliqua. Ut enim ad minim veniam, quis nostrud exercitation.<br><br>Lorem ipsum dolor sit amet, consectetur adipisic-ing elit, sed do eiusmod tempor incididunt ut labore et dolore magna aliqua. Ut enim ad minim veniam, quis nostrud exercitation.</p>
<a class="more" style="left:394px;top:668px">READ MORE</a>

<h2 class="heading" style="left:650px;top:459px">Latest News</h2>
<div class="rule" style="left:649px;top:499px;width:240px"></div>
<div class="news-title" style="top:507px">There are many variations of passages</div>
<div class="photo" role="img" aria-label="Photo of colleagues at a desk" style="left:649px;top:533px;width:68px;height:57px;background:linear-gradient(135deg,#dfe5ec,#8ea1b5)"></div>
<p class="news-text" style="top:530px">The point of using Lorem Ipsum is that it has a more-or-less normal distribution of letters, as opposed..</p>
<div class="news-date" style="top:582px">&#9633; 8 December 2013</div>
<div class="news-title" style="top:607px">All the Lorem Ipsum generators</div>
<div class="photo" role="img" aria-label="Photo of a businessman signing papers" style="left:649px;top:633px;width:68px;height:57px;background:linear-gradient(135deg,#3a3f47,#d6d8dc)"></div>
<p class="news-text" style="top:630px">The point of using Lorem Ipsum is that it has a more-or-less normal distribution of letters, as opposed..</p>
<div class="news-date" style="top:682px">&#9633; 8 December 2013</div>

<h2 class="heading" style="left:138px;top:737px">Who We Are</h2>
<h2 class="heading" style="left:393px;top:737px">Our Values</h2>
<h2 class="heading" style="left:650px;top:737px">What We Do</h2>
<div class="rule" style="left:137px;top:775px;width:239px"></div>
<div class="rule" style="left:391px;top:775px;width:239px"></div>
<div class="rule" style="left:649px;top:775px;width:239px"></div>
<div class="photo" role="img" aria-label="Photo of a team gathered around a laptop" style="left:137px;top:790px;width:237px;height:108px;background:linear-gradient(90deg,#b9a491,#dcd3cb 50%,#9aa8b8)"></div>
<div class="photo" role="img" aria-label="Overhead photo of a meeting around a round table" style="left:391px;top:790px;width:237px;height:108px;background:linear-gradient(90deg,#cfc9c1,#9b928a 50%,#e4e0dc)"></div>
<div class="photo" role="img" aria-label="Photo of a business team standing together" style="left:649px;top:790px;width:237px;height:108px;background:linear-gradient(90deg,#ecebe9,#b8c6d6 50%,#7c7d80)"></div>
<p class="body-text" style="left:137px;top:915px;width:240px">Lorem ipsum dolor sit amet, consectetur adipisicing elit, sed do eiusmod tempor incididunt ut labore et dolore magna aliqua. Ut enim ad minim veniam, quis nostrud exercitation.</p>
<p class="body-text" style="left:391px;top:915px;width:240px">Lorem ipsum dolor sit amet, consectetur adipisicing elit, sed do eiusmod tempor incididunt ut labore et dolore magna aliqua. Ut enim ad minim veniam, quis nostrud exercitation.</p>
<p class="body-text" style="left:649px;top:915px;width:240px">Lorem ipsum dolor sit amet, consectetur adipisicing elit, sed do eiusmod tempor incididunt ut labore et dolore magna aliqua. Ut enim ad minim veniam, quis nostrud exercitation.</p>
<a class="more" style="left:137px;top:988px">READ MORE</a>
<a class="more" style="left:391px;top:988px">READ MORE</a>
<a class="more" style="left:649px;top:988px">READ MORE</a>

<section class="clients">
  <div class="client" style="left:130px"><i></i>Norvalen</div>
  <div class="client" style="left:275px">Quillcrest</div>
  <div class="client" style="left:396px">Brightmoor</div>
  <div class="client" style="left:534px">Ostrava Labs</div>
  <div class="client" style="left:680px">Kelvane</div>
  <div class="client" style="left:800px">Soreno</div>
</section>

<footer class="footer">
  <div class="links">LINKS &nbsp;| &nbsp;LINKS &nbsp;| &nbsp;LINKS &nbsp;| &nbsp;LINKS</div>
  <div class="copy">Copyright © 2013 All rights reserved. &nbsp;Company Name</div>
  <div class="social" style="left:396px" aria-label="Share"><i style="background:#3b5998"></i></div>
  <div class="social" style="left:428px" aria-label="Follow"><i style="background:#33a6d7"></i></div>
  <div class="social" style="left:460px" aria-label="Connect"><i style="background:#1b75b5"></i></div>
  <div class="contact" style="top:24px"><svg width="16" height="12" viewBox="0 0 16 12"><rect width="16" height="12" rx="1" fill="#8a8a8a"/><path d="M0 1l8 6 8-6" stroke="#e4e4e4" stroke-width="1.3" fill="none"/></svg>hello@tarvexa-insight.example</div>
  <div class="contact" style="top:48px"><svg width="16" height="14" viewBox="0 0 24 24"><path fill="#8a8a8a" d="M6.6 10.8a15 15 0 0 0 6.6 6.6l2.2-2.2c.3-.3.7-.4 1-.2 1.1.4 2.3.6 3.6.6.6 0 1 .4 1 1V20c0 .6-.4 1-1 1A17 17 0 0 1 3 4c0-.6.4-1 1-1h3.5c.6 0 1 .4 1 1 0 1.3.2 2.5.6 3.6.1.3 0 .7-.2 1z"/></svg>555-01988-42170</div>
</footer>
</body>
</html>
```